Bref créative
Business cards, letterhead, MS Word letterhead, envelope
Want to be able to print bus cards and stationary, but also want electronic stationary in Word
I need single sided standard sized Business Card [3.5" x 2"]
Myriad Pro family of fonts
Simple
Marion T Fleck
Principal
4312 SW Birch Hollow Lane
Wilsonville, OR 97070
Marionfleck@pellworthadvisory.net
www.pellworthadvisory.net
In addition to the standard formats I would like the finalized letterhead to come to me in MS word format as well.
I'm uploading 2 versions of my logo, with and without the tagline, as the tagline may be too small to read on the bus card or envelope. Would like to see designs with both versions of the logo to see which works best.

```html
<!DOCTYPE html>
<html lang="en">
<head>
<meta charset="utf-8">
<title>Pellworth Advisory Stationery</title>
<link href="https://fonts.googleapis.com/css2?family=Source+Sans+3:wght@400;600;700&display=swap" rel="stylesheet">
<style>
:root{
  --bg:#e4e2df;
  --paper:#ffffff;
  --navy:#1f2a78;
  --navy-deep:#141c5a;
  --green:#7fb53a;
  --ink:#3a3a3a;
  --rule:#9a9a9a;
  --black:#111111;
}
*{box-sizing:border-box;margin:0;padding:0}
html,body{width:1200px;height:554px;overflow:hidden}
body{background:var(--bg);font-family:"Source Sans 3",Arial,sans-serif;color:var(--ink);position:relative}
.piece{position:absolute;background:var(--paper);box-shadow:0 2px 6px rgba(0,0,0,.25);overflow:hidden}
.band{position:absolute;left:0;bottom:0;width:100%;background:linear-gradient(180deg,var(--navy) 0%,var(--navy-deep) 100%)}
.brand{display:flex;align-items:center;gap:4px;color:var(--navy);font-weight:700;white-space:nowrap}
.brand-dot{display:inline-block;background:var(--navy);border-radius:50%;flex:none}
.small{font-size:5px;line-height:7px}

/* cards */
.card{border-radius:6px}
.card-a{left:137px;top:41px;width:120px;height:103px}
.card-b{left:264px;top:41px;width:96px;height:127px}
.card .band{height:18px}
.card .brand{position:absolute;font-size:8px}
.card .brand-dot{width:5px;height:5px}
.card-a .brand{left:9px;top:26px}
.card-a .details{position:absolute;left:68px;top:20px;font-size:4.5px;line-height:6px}
.card-b .brand{left:8px;top:14px;font-size:7px}
.card-b .details{position:absolute;left:8px;top:40px;font-size:4px;line-height:5.5px}
.details .name{font-weight:700;color:var(--navy);font-size:5px}

/* envelopes */
.env-back{left:36px;top:307px;width:300px;height:106px}
.env-back .flap{position:absolute;left:0;top:0;width:100%;height:56px}
.env-back .brand{position:absolute;left:112px;top:22px;font-size:8px}
.env-front{left:144px;top:372px;width:276px;height:127px}
.env-front .brand{position:absolute;left:22px;top:36px;font-size:8px}
.env-front .return{position:absolute;left:22px;top:52px;font-size:4.5px;line-height:6px}
.brand-dot.s{width:5px;height:5px}

/* letterhead & fax */
.sheet{top:31px;width:360px;height:502px}
.letterhead{left:444px}
.fax{left:816px}
.sheet .band{height:30px}
.sheet .brand{position:absolute;left:32px;top:42px;font-size:11px}
.sheet .brand-dot{width:8px;height:8px}
.sheet .contact{position:absolute;left:262px;top:30px}
.sheet .footer{position:absolute;left:34px;bottom:11px;color:#fff;font-size:5px;display:flex;align-items:center;gap:4px}
.footer .dot{width:4px;height:4px;border-radius:50%;background:#fff}

.fax-table{position:absolute;left:30px;top:70px;width:300px;border-collapse:collapse;font-size:6px}
.fax-table th{background:var(--black);color:#fff;text-align:left;font-size:12px;font-weight:700;padding:1px 6px;height:16px}
.fax-table td{border:1px solid var(--rule);height:17px;padding:0 4px;color:#555}
.fax-table td.label{width:40px}
.checks{position:absolute;left:30px;top:166px;width:300px;display:flex;justify-content:space-between;font-size:4.5px;color:#666}
.checks span::before{content:"";display:inline-block;width:4px;height:4px;border:1px solid var(--rule);margin-right:2px;vertical-align:-1px}
</style>
</head>
<body>

<!-- business card, front -->
<div class="piece card card-a">
  <div class="brand"><span class="brand-dot"></span>Pellworth</div>
  <div class="details">
    <div class="name">Marion T Fleck</div>
    <div>Principal</div>
  </div>
  <div class="band" role="img" aria-label="Navy decorative band"></div>
</div>

<!-- business card, details -->
<div class="piece card card-b">
  <div class="brand"><span class="brand-dot"></span>Pellworth Advisory</div>
  <div class="details">
    <div class="name">Marion T Fleck</div>
    <div>Principal</div>
    <div>4312 SW Birch Hollow Lane</div>
    <div>Wilsonville, OR 97070</div>
    <div>P 503.555.0147</div>
    <div>Marionfleck@pellworthadvisory.net</div>
    <div>www.pellworthadvisory.net</div>
  </div>
  <div class="band" role="img" aria-label="Navy decorative band"></div>
</div>

<!-- envelope back -->
<div class="piece env-back">
  <svg class="flap" viewBox="0 0 300 56" preserveAspectRatio="none" aria-hidden="true">
    <path d="M0 0 L150 54 L300 0" fill="none" stroke="#cfcfcf" stroke-width="1"/>
  </svg>
  <div class="brand"><span class="brand-dot s"></span>Pellworth Advisory</div>
</div>

<!-- envelope front -->
<div class="piece env-front">
  <div class="brand"><span class="brand-dot s"></span>Pellworth Advisory</div>
  <div class="return">
    <div>4312 SW Birch Hollow Lane</div>
    <div>Wilsonville, OR 97070</div>
  </div>
</div>

<!-- letterhead -->
<div class="piece sheet letterhead">
  <div class="brand"><span class="brand-dot"></span>Pellworth Advisory</div>
  <div class="contact small">
    <div>4312 SW Birch Hollow Lane</div>
    <div>Wilsonville, OR 97070</div>
    <div>P 503.555.0147</div>
    <div>Marionfleck@pellworthadvisory.net</div>
  </div>
  <div class="band" role="img" aria-label="Navy decorative band"></div>
  <div class="footer"><span class="dot"></span>www.pellworthadvisory.net</div>
</div>

<!-- fax sheet -->
<div class="piece sheet fax">
  <div class="brand"><span class="brand-dot"></span>Pellworth Advisory</div>
  <div class="contact small">
    <div>4312 SW Birch Hollow Lane</div>
    <div>Wilsonville, OR 97070</div>
    <div>P 503.555.0147</div>
    <div>F 503.555.0148</div>
  </div>
  <table class="fax-table">
    <tr><th colspan="4">FAX</th></tr>
    <tr><td class="label">To</td><td></td><td class="label">From</td><td></td></tr>
    <tr><td class="label">Phone</td><td></td><td class="label">Fax</td><td></td></tr>
    <tr><td class="label">Pages</td><td></td><td class="label">Date</td><td></td></tr>
    <tr><td class="label">Re</td><td></td><td class="label">CC</td><td></td></tr>
  </table>
  <div class="checks">
    <span>Urgent</span><span>For Review</span><span>Please Comment</span><span>Please Reply</span><span>Please Recycle</span>
  </div>
  <div class="band" role="img" aria-label="Navy decorative band"></div>
  <div class="footer"><span class="dot"></span>www.pellworthadvisory.net</div>
</div>

</body>
</html>
```